IT Freelancer (Consulting, trainer and project manager) needed letterhead

As a freelancer for IT Trainingswhip, consulting and project management I need a letterhead design. What is desired is a design that fits the existing logo (see Annex). It is functional, reliable, and equal time wirkenn Agil and modern. The whole is in color, as well as printed out to make a good impression on a black and white printer. The whole is to the existing Cooperate design (business card, homepage, logo) fit. Therefore, the choice of colors.

Target Market(s)

Customers such as medium-sized enterprises, training institutions

Industry/Entity Type

Consulting

Colors
0455a3
3277b5
85abd2
cfdfed
34a6d7
32a6d6
249fd4
0792cd
85cae6

Requirements
Must have
• Must include logo (see Annex) address (Ahornweg 14, 84317 Tannenbrunn, Germany). Must seriously and act simultaneously Agil. Design should (even) be adaptable (signature, address, etc.) design must look good on a black / white laser

```html
<!DOCTYPE html>
<html lang="de">
<head>
<meta charset="utf-8">
<title>Konrad Weidner – Briefbogen</title>
<link href="https://fonts.googleapis.com/css2?family=Lato:wght@400;700;900&display=swap" rel="stylesheet">
<style>
  :root {
    --backdrop: #bdbdbd;
    --paper: #ffffff;
    --navy: #0455a3;
    --sky: #34a6d7;
    --ink: #1c1c1c;
    --muted: #333333;
  }
  * { margin: 0; padding: 0; box-sizing: border-box; }
  html, body { width: 1200px; height: 1003px; overflow: hidden; }
  body {
    background: var(--backdrop);
    font-family: "Lato", sans-serif;
    color: var(--ink);
    position: relative;
  }
  .letterhead {
    position: absolute;
    left: 260px; top: 20px;
    width: 680px; height: 962px;
    background: var(--paper);
    overflow: hidden;
  }
  .top-rule {
    position: absolute; left: 0; top: 0; width: 100%; height: 4px;
    background: linear-gradient(90deg, var(--sky), var(--navy));
  }
  .sender-line {
    position: absolute; left: 70px; top: 96px;
    font-size: 7.5px; color: var(--muted); letter-spacing: .1px;
  }
  .contact {
    position: absolute; left: 392px; top: 56px;
    font-size: 10.5px; line-height: 13px; color: var(--muted);
  }
  .contact .gap { height: 6px; }
  .contact-row { display: flex; align-items: center; gap: 6px; }
  .contact-row svg { width: 9px; height: 9px; flex: none; }
  .divider {
    position: absolute; left: 535px; top: 56px; width: 1px; height: 78px;
    background: var(--navy);
  }
  .brand {
    position: absolute; left: 550px; top: 52px; width: 110px;
    display: flex; flex-direction: column; align-items: center; gap: 6px;
  }
  .brand-mark {
    width: 50px; height: 50px; border-radius: 50%; background: var(--navy);
  }
  .brand-name {
    font-weight: 900; color: var(--navy); text-align: center;
    font-size: 15px; line-height: 15px; letter-spacing: .5px;
  }
  .body-copy {
    position: absolute; left: 70px; top: 200px; width: 530px;
    font-size: 11.2px; line-height: 13.6px; color: var(--ink);
  }
  .body-copy p { margin-bottom: 12px; }
  .footer-band { position: absolute; left: 0; bottom: 0; width: 100%; height: 44px; }
  .website {
    position: absolute; right: 60px; bottom: 12px;
    color: #fff; font-size: 12px; letter-spacing: .6px;
  }
</style>
</head>
<body>
  <main class="letterhead">
    <div class="top-rule"></div>

    <div class="sender-line">Konrad Weidner · Ahornweg 14 · 84317 Tannenbrunn · Deutschland</div>

    <div class="contact">
      <div>Ahornweg 14</div>
      <div>84317 Tannenbrunn</div>
      <div>Deutschland</div>
      <div class="gap"></div>
      <div class="contact-row">
        <svg viewBox="0 0 10 10"><path d="M2 1l2 2-1 1.2c.6 1.2 1.6 2.2 2.8 2.8L7 6l2 2-1.4 1.4C4.6 9.2.8 5.4.6 2.4z" fill="var(--navy)"/></svg>
        <span>512 004 2290</span>
      </div>
      <div class="contact-row">
        <svg viewBox="0 0 10 10"><rect x="2" y="1" width="6" height="3" fill="var(--navy)"/><rect x="1" y="4" width="8" height="4" rx="1" fill="var(--navy)"/><rect x="3" y="7" width="4" height="2.5" fill="var(--navy)"/></svg>
        <span>512 004 2291</span>
      </div>
      <div class="contact-row">
        <svg viewBox="0 0 10 10"><rect x="0.5" y="2" width="9" height="6" fill="var(--navy)"/><path d="M0.5 2l4.5 3.5L9.5 2" stroke="#fff" stroke-width="0.9" fill="none"/></svg>
        <span>info@konradweidner.de</span>
      </div>
    </div>

    <div class="divider"></div>

    <div class="brand">
      <div class="brand-mark"></div>
      <div class="brand-name">KONRAD<br>WEIDNER</div>
    </div>

    <section class="body-copy">
      <p>Lorem ipsum dolor sit amet, consectetur adipiscing elit. Praesent non est diam. Vivamus risus sem, gravida sit amet nibh ut, ornare lobortis ante. Aliquam sollicitudin, mauris tincidunt semper venenatis, orci est pretium augue, ut vestibulum felis velit bibendum urna. Integer sollicitudin aliquet ligula, non ultricies nisl efficitur nec. Aliquam felis lorem, facilisis ac condimentum quis, consectetur volutpat lacus. Proin fermentum sem quis elit efficitur, eu tempus magna maximus.</p>
      <p>Aenean a mi tortor. Morbi pretium mi sed cursus vehicula. Lorem ipsum dolor sit amet, consectetur adipiscing elit. In finibus eros ac maximus finibus. Nunc pretium pellentesque tellus. Nullam accumsan nisl non diam commodo sagittis. Nunc et ante sit amet urna auctor convallis. Maecenas sed fringilla metus, sit amet vulputate felis. Morbi eget tempor nisi. Aliquam erat volutpat. Aenean laoreet interdum tempus.</p>
      <p>Maecenas dignissim placerat mauris, vitae sollicitudin ex. Integer bibendum maximus mauris, ac tempor urna viverra id. Integer tincidunt lobortis nisl at posuere. Sed faucibus vulputate finibus. Maecenas convallis, sem quis pellentesque cursus, urna quam aliquam augue, quis porttitor eros est nec lectus. Sed mattis at tellus ut blandit. Aenean nunc magna, viverra sed mauris vel, porta finibus lacus. Nullam bibendum turpis rutrum porta placerat</p>
      <p>Aenean a mi tortor. Morbi pretium mi sed cursus vehicula. Lorem ipsum dolor sit amet, consectetur adipiscing elit. In finibus eros ac maximus finibus. Nunc pretium pellentesque tellus. Nullam accumsan nisl non diam commodo sagittis. Nunc et ante sit amet urna auctor convallis. Maecenas sed fringilla metus, sit amet vulputate felis. Morbi eget tempor nisi. Aliquam erat volutpat. Aenean laoreet interdum tempus. .</p>
    </section>

    <svg class="footer-band" viewBox="0 0 680 44" preserveAspectRatio="none" aria-hidden="true">
      <rect x="0" y="24" width="400" height="20" fill="var(--sky)"/>
      <path d="M318 44 C350 34 362 2 400 2 L680 2 L680 44 Z" fill="var(--navy)"/>
      <path d="M308 44 C342 33 354 0 396 0" stroke="#fff" stroke-width="1.5" fill="none"/>
    </svg>
    <div class="website">www.konradweidner.de</div>
  </main>
</body>
</html>
```